KWM Plumbing and Roofing

design a fresh modern card for a young plumbing business looking to break into the market.
Must include the logo in the attached file
Lowen Fairbrook
Phone number 0412689405
Vic Licence no 63920
email......

New Homes & Renovations
General Plumbing & Maintenance
Solar Hot Water Units
Roofing & Guttering (new and replacement)

Industry/Entity Type

Business

```html
<!DOCTYPE html>
<html lang="en">
<head>
<meta charset="utf-8">
<title>KWM Plumbing and Roofing – Business Card</title>
<link rel="stylesheet" href="https://fonts.googleapis.com/css2?family=Lato:wght@400;700;900&display=swap">
<style>
  :root {
    --blue: #0f5a86;
    --gold: #c8892c;
    --white: #ffffff;
    --ink: #111418;
    --backdrop: #e9e7e3;
  }
  * { box-sizing: border-box; margin: 0; padding: 0; }
  html, body { width: 1200px; height: 1000px; overflow: hidden; }
  body {
    background: var(--backdrop);
    font-family: "Lato", Arial, sans-serif;
    display: flex;
    align-items: center;
    justify-content: center;
    gap: 80px;
  }
  .card {
    width: 360px;
    height: 620px;
    background: var(--white);
    box-shadow: 0 10px 30px rgba(0,0,0,.18);
    position: relative;
    overflow: hidden;
  }
  /* Front */
  .card-front { display: flex; flex-direction: column; align-items: center; justify-content: center; }
  .brand { display: flex; flex-direction: column; align-items: center; gap: 18px; }
  .brand-dot { width: 150px; height: 150px; border-radius: 50%; background: var(--blue); }
  .brand-name {
    color: var(--blue); font-weight: 900; font-size: 26px; text-align: center; line-height: 1.2;
  }
  .licence {
    position: absolute; right: 22px; bottom: 18px;
    color: var(--blue); font-weight: 700; font-size: 15px;
  }
  /* Back */
  .card-back { display: flex; flex-direction: column; }
  .back-top { height: 330px; padding: 46px 20px 0; display: flex; flex-direction: column; align-items: center; }
  .brand-small { display: flex; align-items: center; gap: 12px; }
  .brand-small .brand-dot { width: 44px; height: 44px; }
  .brand-small .brand-name { font-size: 22px; text-align: left; }
  .services { margin-top: 26px; list-style: none; text-align: center; color: var(--ink); font-size: 16px; font-weight: 700; line-height: 1.25; }
  .name-band {
    background: var(--blue); color: var(--white);
    font-size: 28px; font-weight: 400; letter-spacing: .5px;
    text-align: center; padding: 12px 0; text-transform: uppercase;
  }
  .contact { flex: 1; background: var(--gold); padding: 36px 20px 0; text-align: center; }
  .contact dt { color: var(--ink); font-weight: 700; font-size: 21px; }
  .contact dd { color: var(--white); font-size: 23px; margin-bottom: 26px; }
</style>
</head>
<body>
  <section class="card card-front">
    <div class="brand">
      <div class="brand-dot"></div>
      <div class="brand-name">KWM Plumbing<br>and Roofing</div>
    </div>
    <p class="licence">Vic Licence no 63920</p>
  </section>

  <section class="card card-back">
    <div class="back-top">
      <div class="brand brand-small">
        <div class="brand-dot"></div>
        <div class="brand-name">KWM Plumbing<br>and Roofing</div>
      </div>
      <ul class="services">
        <li>New Homes &amp; Renovations</li>
        <li>General Plumbing &amp; Maintenance</li>
        <li>Solar Hot Water Units</li>
        <li>Roofing &amp; Guttering (New and Replacement)</li>
      </ul>
    </div>
    <div class="name-band">Lowen Fairbrook</div>
    <dl class="contact">
      <dt>Phone:</dt>
      <dd>0412689405</dd>
      <dt>Email:</dt>
      <dd>lowenfairbrook@kwm.com</dd>
    </dl>
  </section>
</body>
</html>
```